TrevanHollis's Signature Beard Oil Label Design

I'm looking for a creative designer to run with the design. I am not sure what I really want so surprise me. What ever you do please use earth tone colors. The bottles I use is 2.0 ounces. It is a Boston amber bottle with glass dropper. It is 1.5 width by 3.75 inch height. :Benefits : * Organic * Hair growth* Repairs Split Ends* Softens * Health Shine* Aromatherapy fragrance* Reduce Itching/Irritation * Reduce Dandruff* Reduces Flyaway hair Directions: Place a nickel size drop into palm of handMassage into beard 2 to 3 times a day

Target Market(s)

MEN WITH BEARDS AND MEN THAT WANT TO GROW BEARDS BUT DON'T KNOW HOW

Industry/Entity Type

Hair Care Product

Font styles to use
Serif
Script

Colors
1b1b1b
fdf9cf
ffc214
ffffff

Requirements
Must have
• FALL COLOR SCHEME, Trevan Hollis written in a fancy cursive script, all others can me different, please use the gold lion logo without the word Lion.
Nice to have
• CLASSY, MANLY, OLD AND NEW SCHOOL ESSENCE
Should not have
• Anything feminine, Flint Cove

```html
<!DOCTYPE html>
<html lang="en">
<head>
<meta charset="utf-8">
<title>Trevan Hollis Signature Beard Oil Label</title>
<link href="https://fonts.googleapis.com/css2?family=Great+Vibes&family=Stint+Ultra+Condensed&display=swap" rel="stylesheet">
<style>
  :root {
    --ink: #1b1b1b;
    --label-black: #0f0e0d;
    --cream: #fdf9cf;
    --gold: #ffc214;
    --gold-deep: #c9871a;
    --white: #ffffff;
    --page: #ffffff;
  }
  html, body {
    margin: 0;
    padding: 0;
    width: 1032px;
    height: 1200px;
    overflow: hidden;
    background: var(--page);
  }
  .canvas {
    position: relative;
    width: 1032px;
    height: 1200px;
  }
  .label {
    position: absolute;
    left: 176px;
    top: 50px;
    width: 680px;
    height: 1100px;
    background: radial-gradient(ellipse at 55% 45%, #26221f 0%, var(--label-black) 70%);
    overflow: hidden;
  }
  .brand-rule {
    position: absolute;
    left: 122px;
    top: 110px;
    width: 3px;
    height: 930px;
    background: var(--white);
  }
  .brand-name {
    position: absolute;
    left: 66px;
    top: 575px;
    transform: translate(-50%, -50%) rotate(-90deg);
    font-family: "Great Vibes", cursive;
    font-size: 118px;
    line-height: 1;
    color: var(--white);
    white-space: nowrap;
  }
  .flourish {
    position: absolute;
    left: 185px;
    width: 190px;
    height: 34px;
  }
  .flourish--top { top: 150px; }
  .flourish--bottom { top: 1030px; }
  .crest {
    position: absolute;
    left: 485px;
    top: 40px;
    width: 180px;
    height: 350px;
  }
  .benefits {
    position: absolute;
    left: 160px;
    top: 205px;
    margin: 0;
    padding: 0;
    list-style: none;
    font-family: "Stint Ultra Condensed", serif;
    font-size: 66px;
    line-height: 91px;
    color: var(--white);
    letter-spacing: 1px;
    text-transform: uppercase;
    white-space: nowrap;
  }
  .benefits li::before {
    content: "*";
    font-size: 40px;
    vertical-align: top;
    margin-right: 10px;
    position: relative;
    top: -6px;
  }
</style>
</head>
<body>
<div class="canvas">
  <section class="label">
    <div class="brand-name">Trevan Hollis</div>
    <div class="brand-rule"></div>

    <svg class="flourish flourish--top" role="img" aria-label="Decorative scroll flourish" viewBox="0 0 190 34">
      <rect x="0" y="15" width="190" height="4" rx="2" fill="var(--cream)" opacity="0.85"/>
    </svg>

    <svg class="crest" role="img" aria-label="Gold rampant lion illustration" viewBox="0 0 180 350">
      <defs>
        <linearGradient id="crestGold" x1="0" y1="0" x2="1" y2="1">
          <stop offset="0" stop-color="var(--gold)"/>
          <stop offset="1" stop-color="var(--gold-deep)"/>
        </linearGradient>
      </defs>
      <rect x="0" y="0" width="180" height="350" rx="36" fill="url(#crestGold)" opacity="0.9"/>
    </svg>

    <ul class="benefits">
      <li>Organic</li>
      <li>Hair Growth</li>
      <li>Repairs Split Ends</li>
      <li>Softens</li>
      <li>Health Shine</li>
      <li>Aromatherapy</li>
      <li>Reduce Irritation</li>
      <li>Reduce Dandruff</li>
      <li>Reduces Flyaway Hair</li>
    </ul>

    <svg class="flourish flourish--bottom" role="img" aria-label="Decorative scroll flourish" viewBox="0 0 190 34">
      <rect x="0" y="15" width="190" height="4" rx="2" fill="var(--cream)" opacity="0.85"/>
    </svg>
  </section>
</div>
</body>
</html>
```